Valdarossi’s Artisan Pizzeria Menu Contest

I’m looking for a menu design for a new pizzeria - it’s farm to table type of restaurant - more upscale than a typical pizzeria - white washed wood interior with some industrial accents - I am looking for a creative menu layout using the attached sample menu items -
Valdarossi’s is an artisanal pizzeria with an atmosphere that will make you feel at home for any situation, first date, anniversary, business lunch, boys night out or girls night out with a menu inspired by the idea of a simple honest cooking paired with fresh – quality ingredients. Full service dining experience that is still casual but dedicated to extraordinary hospitality.
While developing the menu we have created a network of amazing farms and purveyors to supply our restaurant with fresh milled 100% California flour for our hand crafted dough, as well as sustainably farmed organic produce, meats and cheeses.
The menu includes classics like the Margherita pizza to daily seasonal specials, fresh salads to rustic small plates including moms meatball recipe to a fresh local burrata with handmade bread. Each dish reflects our passion for sourcing the freshest quality local ingredients.
To compliment the menu, Valdarossi’s serves an extensive wine list with selections focusing on Italian varietals. The cocktail program has been carefully crafted to offer something to entice ever palate and the beer list has unique selections of the world’s finest brewers.
Target Market(s)
25-45 year old men and women
Industry/Entity Type
American Restaurant
Requirements
Must have
- professional tone
Nice to have
- a balance of elegance and industrial (rustic)
Should not have
- photos or playful graphics etc..

```html
<!DOCTYPE html>
<html lang="en">
<head>
<meta charset="utf-8">
<title>Valdarossi’s Artisan Pizzeria Menu</title>
<link rel="stylesheet" href="https://fonts.googleapis.com/css2?family=Roboto:wght@400;500&family=Montserrat:wght@500&display=swap">
<style>
  :root {
    --page-bg: #ececec;
    --menu-bg: #050505;
    --accent-red: #e8202a;
    --photo-red-light: #e5333b;
    --photo-red-dark: #7a0b10;
    --text-light: #f2f2f2;
  }
  * { margin: 0; padding: 0; box-sizing: border-box; }
  html, body {
    width: 1200px; height: 801px; overflow: hidden;
    background: var(--page-bg);
    font-family: "Roboto", Arial, sans-serif;
  }
  .menu {
    position: absolute; left: 330px; top: 18px;
    width: 540px; height: 764px;
    background: var(--menu-bg);
    color: var(--text-light);
    overflow: hidden;
  }
  .hero-photo {
    position: absolute; left: 0; top: 0; width: 540px; height: 268px;
    background:
      radial-gradient(ellipse at 50% 35%, rgba(255,90,90,0.35), transparent 60%),
      linear-gradient(180deg, var(--photo-red-light) 0%, #c81f27 55%, var(--photo-red-dark) 100%);
  }
  .brand-name {
    position: absolute; left: 0; width: 540px; top: 108px;
    text-align: center;
    font-family: "Roboto", Arial, sans-serif;
    font-weight: 500; font-size: 38px; letter-spacing: 1px;
    color: #ffffff;
  }
  .menu-title {
    position: absolute; left: 0; width: 540px; top: 232px;
    text-align: center;
    font-family: "Montserrat", Arial, sans-serif;
    font-weight: 500; font-size: 28px; letter-spacing: 20px;
    padding-left: 20px;
    color: #ffffff; line-height: 34px;
  }
  .column-divider {
    position: absolute; left: 266px; top: 287px;
    width: 1px; height: 460px; background: var(--accent-red);
  }
  .section { position: absolute; width: 180px; }
  .section.left { left: 61px; }
  .section.right { left: 302px; }
  .section-heading {
    color: var(--accent-red);
    font-weight: 500; font-size: 13px; line-height: 18px;
    letter-spacing: 0.2px;
  }
  .items { list-style: none; }
  .items li {
    position: relative;
    font-size: 10.8px; line-height: 19.75px;
  }
  .items .price { position: absolute; left: 144px; top: 0; }
</style>
</head>
<body>
<main class="menu">
  <div class="hero-photo" role="img" aria-label="Red-toned photograph of the restaurant dining room with tables, chairs and hanging lights"></div>
  <div class="brand-name">Valdarossi’s</div>
  <h1 class="menu-title">MENU</h1>

  <div class="column-divider"></div>

  <section class="section left" style="top:291px">
    <h2 class="section-heading">APPETIZERS</h2>
    <ul class="items" style="margin-top:6px">
      <li>Brussels<span class="price">$10.00</span></li>
      <li>Meatballs<span class="price">$13.00</span></li>
      <li>Mussels<span class="price">$15.00</span></li>
      <li>Romanesco<span class="price">$11.00</span></li>
      <li>Chicken wings<span class="price">$10.00</span></li>
      <li>Burrata<span class="price">$13.00</span></li>
    </ul>
  </section>

  <section class="section left" style="top:439px">
    <h2 class="section-heading">SALADS</h2>
    <ul class="items" style="margin-top:6px">
      <li>Chopped Salad<span class="price">$13.00</span></li>
      <li>Caesar Salad<span class="price">$11.00</span></li>
      <li>Farm Salad<span class="price">$15.00</span></li>
      <li>Grilled Little Gem<span class="price">$11.00</span></li>
      <li>Spinach and Arugula Salad<span class="price">$12.00</span></li>
    </ul>
  </section>

  <section class="section left" style="top:566px">
    <h2 class="section-heading">DAILY SOUP</h2>
    <ul class="items" style="margin-top:5px">
      <li>Example Tomato bisque<span class="price">$8.00</span></li>
    </ul>
  </section>

  <section class="section left" style="top:620px">
    <h2 class="section-heading">SANDWICHES</h2>
    <ul class="items" style="margin-top:0">
      <li>Italian Sub<span class="price">$13.00</span></li>
      <li>Turkey Sandwich<span class="price">$12.00</span></li>
      <li>Meatball Sub<span class="price">$13.00</span></li>
      <li>Harvest Burger<span class="price">$14.00</span></li>
      <li>Chicken Sandwich<span class="price">$13.00</span></li>
    </ul>
  </section>

  <section class="section right" style="top:291px">
    <h2 class="section-heading">PIZZAS</h2>
    <ul class="items" style="margin-top:6px">
      <li>Margherita<span class="price">$14.00</span></li>
      <li>Organic Sausage<span class="price">$16.00</span></li>
      <li>Pepperoni<span class="price">$16.00</span></li>
      <li>Salumi and Burrata<span class="price">$17.00</span></li>
      <li>Daily special<span class="price">$17.00</span></li>
      <li>Mushroom<span class="price">$15.00</span></li>
      <li>Prosciutto and egg<span class="price">$16.00</span></li>
      <li>Quarttro Formaggi<span class="price">$15.00</span></li>
      <li>Farmers Pizza<span class="price">$17.00</span></li>
      <li>Keto friendly<span class="price">$17.00</span></li>
    </ul>
  </section>

  <section class="section right" style="top:526px">
    <h2 class="section-heading">CRUSTS</h2>
    <ul class="items" style="margin-top:5px">
      <li>Traditional</li>
      <li>Gluten free<span class="price">$3.00</span></li>
      <li>Cauliflower<span class="price">$3.00</span></li>
    </ul>
  </section>

  <section class="section right" style="top:624px">
    <h2 class="section-heading">DIPS</h2>
    <ul class="items" style="margin-top:7px">
      <li>Ranch<span class="price">$1.00</span></li>
      <li>Tomato Sauce<span class="price">$1.00</span></li>
      <li>Spicy Dip<span class="price">$1.00</span></li>
      <li>Blue Cheese<span class="price">$1.00</span></li>
    </ul>
  </section>
</main>
</body>
</html>
```